Buttons, Banners & MPUs - 'Coastal Getaway Digest'

We are launching a new product - a bookazine on sale later this month!

General description below:

COASTAL GETAWAY DIGESTS 2015

Calling all lovers of French holidays! Where will you go in 2015?

Let us guide you to the very best holidays in France with our brand new guide, featuring 180 pages of high quality and inspiring editorial and imagery. Coastal Getaways Digests 2015 provides a comprehensive, ideas-packed guide to classic breaks, as well as niche and new holiday ideas across France.

Love to get out in the French fresh air? We have activities such as boating, cycling and golf covered. There’s plenty for culture vultures and city breakers, too, plus lots of great ideas for family breaks including theme parks, zoos and attractions.

We whet the appetite of foodies and wine lovers, provide a guide to markets and festivals and also get off the beaten track with guides to driving, railway holidays and visit some of France’s most beautiful villages. And if you want to get creative, there are loads of ideas for photography, art, ‘me time’ escapes and tempting snapshots of some of France’s most unusual accommodation.

Whatever you love about France, there’s a fabulous Coastal Getaway Digest made for you!

Design brief - bright, fun, exciting, inspiring.. with a clear call-to-action

We require a variety of sizes including:
300 x 250, 250 x 250, 728 x 90, 468 x 60, 120 x 600, 120 x 240, 600 x 200
- please only create a couple to showcase your design

More information can be found on the products website but please be aware that this is still under construction so please do not base your design on this: http://www.coastalgetawaydigests.example/

Target Market(s)

Francophiles, holiday makers, 40+, families, couples,

Industry/Entity Type

Construction

Font styles to use
Serif
Sans Serif

Requirements
Must have
• Logo
• Call to action
Nice to have
• Suggested strap lines:
• - The ultimate guide to holidays in France
• - The biggest and best guide to France
• - 180 pages of Fabulous Coastal Getaway Digest Ideas
• - What's New in 2015
Should not have
• Price - we want to direct traffic to our website which will reflect their local currency

```html
<!DOCTYPE html>
<html lang="en">
<head>
<meta charset="utf-8">
<title>Coastal Getaway Digest – Banner Set</title>
<link href="https://fonts.googleapis.com/css2?family=Arimo:wght@400;700&display=swap" rel="stylesheet">
<style>
:root{
  --page:#efe9e2;
  --blue:#1c64ad;
  --blue-deep:#15528f;
  --yellow:#ffe01a;
  --white:#ffffff;
  --navy:#2b2a7c;
  --navy-text:#2a2a80;
  --sky-top:#4f8fd6;
  --sky-low:#bfe0f2;
  --sea:#3fc3c9;
  --sand:#efe6d8;
  --ink:#222;
}
*{margin:0;padding:0;box-sizing:border-box}
html,body{width:1200px;height:900px;overflow:hidden}
body{background:var(--page);font-family:"Arimo",Arial,sans-serif;position:relative}
.banner{position:absolute;overflow:hidden;background:var(--blue)}
.photo{position:absolute;background:linear-gradient(180deg,var(--sky-top) 0%,var(--sky-low) 45%,var(--sea) 62%,var(--sand) 74%,var(--sand) 100%)}
.brand{color:var(--white);font-weight:700;line-height:1;white-space:nowrap}
.brand-year{display:block;color:var(--white);font-weight:700;text-align:right;white-space:nowrap}
.kicker{color:var(--yellow);font-weight:700;text-transform:uppercase;white-space:nowrap}
.strap{color:var(--white);font-weight:700;line-height:1.05}
.strap .hi{color:var(--yellow)}
.cta{position:absolute;background:var(--navy);color:var(--white);font-weight:700;text-align:center;border-radius:4px;border:1px solid #4b4aa8;white-space:nowrap}
.url{position:absolute;font-weight:400;white-space:nowrap}

/* leaderboard 728x90 */
.leaderboard{left:197px;top:40px;width:853px;height:105px;background:linear-gradient(90deg,var(--blue-deep),var(--blue) 40%,var(--blue-deep))}
.leaderboard .photo{left:0;top:0;width:240px;height:105px;-webkit-mask-image:linear-gradient(90deg,#000 70%,transparent);mask-image:linear-gradient(90deg,#000 70%,transparent)}
.leaderboard .strap{position:absolute;left:204px;top:16px;font-size:25px;white-space:nowrap}
.leaderboard .strap .hi{font-size:35px}
.leaderboard .kicker{position:absolute;left:622px;top:4px;font-size:8.5px}
.leaderboard .brand{position:absolute;left:624px;top:15px;font-size:25px;letter-spacing:-0.8px}
.leaderboard .brand-year{position:absolute;left:622px;top:41px;width:208px;font-size:9px}
.leaderboard .cta{left:652px;top:56px;width:142px;height:30px;line-height:28px;font-size:15px}
.leaderboard .url{left:640px;top:90px;font-size:11px;color:var(--white)}

/* square 300x250 */
.square{left:268px;top:282px;width:394px;height:328px}
.square .kicker{position:absolute;left:6px;top:3px;font-size:13.5px}
.square .brand{position:absolute;left:16px;top:22px;font-size:43px;letter-spacing:-1.2px}
.square .brand-year{position:absolute;left:0;top:70px;width:372px;font-size:14px}
.square .photo{left:0;top:88px;width:394px;height:240px;background:linear-gradient(180deg,var(--sky-top) 0%,var(--sky-low) 55%,var(--sea) 70%,var(--sand) 80%)}
.square .strap{position:absolute;left:4px;top:112px;width:150px;text-align:center;font-size:19px;color:var(--navy-text)}
.square .strap .hi{font-size:28px;color:var(--yellow)}
.square .cta{left:116px;top:270px;width:168px;height:37px;line-height:35px;font-size:17px}
.square .url{left:112px;top:311px;font-size:12px;color:var(--ink)}

/* skyscraper 120x600 */
.skyscraper{left:759px;top:176px;width:188px;height:703px;background:linear-gradient(180deg,var(--blue-deep),var(--blue) 60%)}
.skyscraper .kicker{position:absolute;left:7px;top:60px;font-size:7.3px}
.skyscraper .brand{position:absolute;left:6px;top:72px;font-size:21px;letter-spacing:-0.6px}
.skyscraper .brand-year{position:absolute;left:0;top:96px;width:178px;font-size:9px}
.skyscraper .strap{position:absolute;left:0;top:186px;width:188px;text-align:center;font-size:24px}
.skyscraper .strap .hi{font-size:35px}
.skyscraper .photo{left:0;top:370px;width:188px;height:333px;background:linear-gradient(180deg,var(--blue) 0%,var(--sky-low) 30%,var(--sea) 52%,var(--sand) 66%)}
.skyscraper .cta{left:12px;top:636px;width:164px;height:38px;line-height:36px;font-size:18px}
.skyscraper .url{left:3px;top:680px;font-size:12px;color:var(--ink)}
</style>
</head>
<body>

<section class="banner leaderboard" aria-label="Leaderboard banner">
  <div class="photo" role="img" aria-label="Family walking hand in hand along a sunny beach"></div>
  <p class="strap">The <span class="hi">BIGGEST</span> and <span class="hi">BEST</span><br>Guide to <span class="hi">FRANCE</span></p>
  <p class="kicker">The ultimate guide to holidays in France</p>
  <p class="brand">Coastal Getaway</p>
  <span class="brand-year">Digest 2015</span>
  <a class="cta">FIND OUT MORE</a>
  <span class="url">coastalgetawaydigests.example</span>
</section>

<section class="banner square" aria-label="Square banner">
  <p class="kicker">The ultimate guide to holidays in France</p>
  <p class="brand">Coastal Getaway</p>
  <span class="brand-year">Digest 2015</span>
  <div class="photo" role="img" aria-label="Family walking hand in hand along a sunny beach by turquoise sea"></div>
  <p class="strap">The<br><span class="hi">BIGGEST</span><br>and <span class="hi">BEST</span><br>Guide to<br><span class="hi">FRANCE</span></p>
  <a class="cta">FIND OUT MORE</a>
  <span class="url">coastalgetawaydigests.example</span>
</section>

<section class="banner skyscraper" aria-label="Skyscraper banner">
  <p class="kicker">The ultimate guide to holidays in France</p>
  <p class="brand">Coastal Getaway</p>
  <span class="brand-year">Digest 2015</span>
  <p class="strap">The<br><span class="hi">BIGGEST</span><br>and <span class="hi">BEST</span><br>Guide to<br><span class="hi">FRANCE</span></p>
  <div class="photo" role="img" aria-label="Family walking hand in hand along a sunny beach"></div>
  <a class="cta">FIND OUT MORE</a>
  <span class="url">coastalgetawaydigests.example</span>
</section>

</body>
</html>
```